3 -4 PAGE GIFT CERTIFICATE REDEMPTION WEBSITE REVAMP

I am revamping the entire website at www.brightperkcentral.net

Will have brand new theme and new logo. Name Of Company:
Bonus Gratuity Dispatch Network
BGDN

OVERVIEW:
I NEED A 3-4 PAGE WEBSITE DESIGNED WITH CHECKOUT MODULE.
My company offers fully brandable and personalizable gift certificates good for travel, vacations, dining rewards, rebates, electronic gifts, etc. and I need to redesign the website where the fulfillment and redemption happens.

So the way it works is a business uses my online platform to create, brand and personalize these gift certificates. The business can brand the certificates in the upper right hand corner of each certificate where the “Compliments Of” area sits with their company logo, website, contact info, etc and can also personalize each individual gift certificate to a specific customer too. SEE EXAMPLE ATTACHED TO BRIEF.

The example I attached to this brief includes a logo which is really just a picture and under it there is 3 lines of text where the business can put a website, phone number and email.

On the left side of the top banner image you will see “Exclusively For”.

So now, after a customer enters their certificate ID #, the branding on the next page must match the Compliments Of area and also must personalize the Sales Page to the customer that is in the Exclusively For” area of the certificate…...

Page 1: LANDING PAGE
CONTENT:

Welcome to the online redemption source for vacation certificates, travel vouchers, digital electronic products, dining incentives, gas and grocery rewards and more!

ENTER YOUR CERTIFICATE ID #
ENTER YOUR EMAIL

Welcome to the online redemption system for vacation certificates, travel vouchers, rebates, digital products, dining incentives, gas and grocery rewards and more!

PLEASE ENTER A VALID CERTIFICATE ID NUMBER TO VIEW THE DETAILS AND TO REDEEM AND ACTIVATE YOUR SPECIAL OFFER.

Also we need a testimonial module ON THIS PAGE AND SALES PAGE

PAGE 2: SALES PAGE FOR OFFER (we will use the 1-4 Night Las Vegas Hotel Stay Certificate)
INSTRUCTIONS EXPLANATION FOR DESIGNER: Every gift certificate has a "Compliments Of Area" in the upper right hand corner....SEE SAMPLE ATTACHED TO BRIEF. On the sales page we also show this to the customer after they enter the code. Every certificate has a Compliments Of area and we will also add "Exclusively For" so the person that is giving the certificate away can specify the name of the recipient so we will also transffer this information over to the SALES PAGE.

CONTENT FOR SALES PAGE:

WELCOME ~~NAME OF PERSON IN EXCLUSIVELY FOR AREA ON CERTIFICATE~~ !!

THIS SPECIAL INCENTIVE OFFER IS COMPLIMENTS OF

~~LOGO THAT IS SEEN ON CERTIFICATE~~
~~TEXT LINE 1~~
~~TEXT LINE 2~~
~~TEXT LINE 3~~

TITLE OF OFFER: STAY & PLAY IN LAS VEGAS FOR UP TO 4 NIGHTS!
There is no doubt that Las Vegas is one of the hottest travel destinations around the world. In fact, some people would even go as far as saying that perhaps it is THE hottest place to visit. Enjoy up to 4 nights of resort/casino accommodations in exciting Las Vegas, NV. Millions of people travel to this exciting city each year to enjoy its thrills. Thanks to the business you received this certificate from, now you can enjoy Las Vegas, NV too!

Features:
*Travel 7 Days A Week
*Stay Your Choice Of Nights (1-4 Nights)
*Good For Two Adults & Two Children
*Pay Just The Taxes & Fees
*Multiple Travel Date Requests Allowed
*Fully Transferable To Another Person
*Just A 30 Days Advance Notice Required
*You Will Have 12 Months To Complete Travel

HOW CAN WE DO THIS?

We contract with the world leading hotel chains and resorts to help them fill their otherwise empty rooms.

We help fill empty rooms which the hotels, resorts and cruise lines turn into additional revenue from other areas of their property and future bookings.

Hotels rarely experience full occupancy, yet they remain open, providing rooms and services at fixed costs. So when hotels give out their rooms by partnering with marketing companies like us, they might miss out on the room fee, but they already didn't have that in the first place, at least now they have the opportunity to gain a customer for their in-house restaurants, room service, their casinos, an extra day stay, future bookings, etc.

The magic of why our program works so well is the fact that it’s a win win for everyone involved. You win because you received a huge savings. The business who gave you the certificate wins because now you will remember them the next time you need the same kind of product or service that they provide and you might even refer your friends and family members. The hotels and resorts win because they gain additional revenue from other areas of their establishment that they otherwise would not have been able to get and they also have a new client that may book with them in the future. Remember, they didn’t have anyone in the room in the first place so since you are paying the normal rack rate you might be more inclined to spend your money at the hotel. You are never under any obligation to do so though!

Retail Value: Up to $826.00 (based on $159.00 per night)

How it Works:
You will receive up to 4 nights in a 3 star or better Las Vegas resort and casino for up to 4 travelers, 2 adults and 2 children.

Simply redeem the certificate to activate the travel period for 1 year. This means you will have at least 1 year to travel from the date you redeem and activate your offer. Be sure to redeem your certificate before it expires! All certificates will have an accompanying expiration date attached to them.

When you are ready to book you will simply have to pay the daily room rate taxes and fees of approximately $12-$33 per night (not per person). On average the taxes and fees come out to about $19 per night. (Retail Value: Up to $826.00 based on $159.00 per night)

Step 1: Redeem your certificate to activate your offer

Step 2: Fill out the online reservation request form with travel dates within the next 12 months.

Step 3: Wait for a confirmation of your booked reservation. You will be notified immediately upon us booking your reservation.

Go on your vacation and thank the business who gave you this special offer by doing business with them again and referring your friends and family members!

No timeshares or sales presentations, Guaranteed!

PAGE 3 IS CHECKOUT PAGE:

PLEASE USE ****HERE IS SAMPLE CODE FOR YOU TO TEST OUT AT CURRENT REDEMPTION PROCESS WWW.BRIGHTPERKCENTRAL.NET 40613-27149

TO SEE THE CURRENT CHECK OUT. I NEED ALL THE SAME CONTENT JUST A DIFFERENT MORE EFFICIENT CHECKOUT PROCESS HERE. OMIT THE LEFT SIDE OF THE CURRENT CHECK OUT PROCESS AS THIS CURRENT PROCESSS IS ONE STEP AND DOES NOT HAVE A SALES PAGE BUT NOW I AM CREATING A SALES PAGE BEFORE THE CHECKOUT SO THE BRANDING AND PERSONALIZATION WILL HAPPEN ON THE SALES PAGE….THANK YOU

Target Market(s)

END USERS THAT ARE REDEEMING SPECIAL OFFERS GIFT CERTIFICATES

Industry/Entity Type

Marketing

Number of Pages Required

4 page

Colors

Designer to choose colors to be used in the design.

Requirements
Must have
• OVERVIEW:
• I NEED A 3-4 PAGE WEBSITE DESIGNED WITH CHECKOUT MODULE.
• My company offers fully brandable and personalizable gift certificates good for travel, vacations, dining rewards, rebates, electronic gifts, etc. and I need to redesign the website where the fulfillment and redemption happens.
• So the way it works is a business uses my online platform to create, brand and personalize these gift certificates. The business can brand the certificates in the upper right hand corner of each certificate where the “Compliments Of” area sits with their company logo, website, contact info, etc and can also personalize each individual gift certificate to a specific customer too. SEE EXAMPLE ATTACHED TO BRIEF.
• The example I attached to this brief includes a logo which is really just a picture and under it there is 3 lines of text where the business can put a website, phone number and email.
• On the left side of the top banner image you will see “Exclusively For”.
• So now, after a customer enters their certificate ID #, the branding on the next page must match the Compliments Of area and also must personalize the Sales Page to the customer that is in the Exclusively For” area of the certificate…...
• Page 1: LANDING PAGE
• CONTENT:
• Welcome to the online redemption source for vacation certificates, travel vouchers, digital electronic products, dining incentives, gas and grocery rewards and more!
• ENTER YOUR CERTIFICATE ID #
• ENTER YOUR EMAIL
• Welcome to the online redemption system for vacation certificates, travel vouchers, rebates, digital products, dining incentives, gas and grocery rewards and more!
• PLEASE ENTER A VALID CERTIFICATE ID NUMBER TO VIEW THE DETAILS AND TO REDEEM AND ACTIVATE YOUR SPECIAL OFFER.
• Also we need a testimonial module ON THIS PAGE AND SALES PAGE
• PAGE 2: SALES PAGE FOR OFFER (we will use the 1-4 Night Las Vegas Hotel Stay Certificate)
• INSTRUCTIONS EXPLANATION FOR DESIGNER: Every gift certificate has a "Compliments Of Area" in the upper right hand corner....SEE SAMPLE ATTACHED TO BRIEF. On the sales page we also show this to the customer after they enter the code. Every certificate has a Compliments Of area and we will also add "Exclusively For" so the person that is giving the certificate away can specify the name of the recipient so we will also transffer this information over to the SALES PAGE.
• CONTENT FOR SALES PAGE:
• WELCOME ~~NAME OF PERSON IN EXCLUSIVELY FOR AREA ON CERTIFICATE~~ !!
• THIS SPECIAL INCENTIVE OFFER IS COMPLIMENTS OF
• ~~LOGO THAT IS SEEN ON CERTIFICATE~~
• ~~TEXT LINE 1~~
• ~~TEXT LINE 2~~
• ~~TEXT LINE 3~~
• TITLE OF OFFER: STAY & PLAY IN LAS VEGAS FOR UP TO 4 NIGHTS!
• There is no doubt that Las Vegas is one of the hottest travel destinations around the world. In fact, some people would even go as far as saying that perhaps it is THE hottest place to visit. Enjoy up to 4 nights of resort/casino accommodations in exciting Las Vegas, NV. Millions of people travel to this exciting city each year to enjoy its thrills. Thanks to the business you received this certificate from, now you can enjoy Las Vegas, NV too!
• Features:
• *Travel 7 Days A Week
• *Stay Your Choice Of Nights (1-4 Nights)
• *Good For Two Adults & Two Children
• *Pay Just The Taxes & Fees
• *Multiple Travel Date Requests Allowed
• *Fully Transferable To Another Person
• *Just A 30 Days Advance Notice Required
• *You Will Have 12 Months To Complete Travel
• HOW CAN WE DO THIS?
• We contract with the world leading hotel chains and resorts to help them fill their otherwise empty rooms.
• We help fill empty rooms which the hotels, resorts and cruise lines turn into additional revenue from other areas of their property and future bookings.
• Hotels rarely experience full occupancy, yet they remain open, providing rooms and services at fixed costs. So when hotels give out their rooms by partnering with marketing companies like us, they might miss out on the room fee, but they already didn't have that in the first place, at least now they have the opportunity to gain a customer for their in-house restaurants, room service, their casinos, an extra day stay, future bookings, etc.
• The magic of why our program works so well is the fact that it’s a win win for everyone involved. You win because you received a huge savings. The business who gave you the certificate wins because now you will remember them the next time you need the same kind of product or service that they provide and you might even refer your friends and family members. The hotels and resorts win because they gain additional revenue from other areas of their establishment that they otherwise would not have been able to get and they also have a new client that may book with them in the future. Remember, they didn’t have anyone in the room in the first place so since you are paying the normal rack rate you might be more inclined to spend your money at the hotel. You are never under any obligation to do so though!
• Retail Value: Up to $826.00 (based on $159.00 per night)
• How it Works:
• You will receive up to 4 nights in a 3 star or better Las Vegas resort and casino for up to 4 travelers, 2 adults and 2 children.
• Simply redeem the certificate to activate the travel period for 1 year. This means you will have at least 1 year to travel from the date you redeem and activate your offer. Be sure to redeem your certificate before it expires! All certificates will have an accompanying expiration date attached to them.
• When you are ready to book you will simply have to pay the daily room rate taxes and fees of approximately $12-$33 per night (not per person). On average the taxes and fees come out to about $19 per night. (Retail Value: Up to $826.00 based on $159.00 per night)
• Step 1: Redeem your certificate to activate your offer
• Step 2: Fill out the online reservation request form with travel dates within the next 12 months.
• Step 3: Wait for a confirmation of your booked reservation. You will be notified immediately upon us booking your reservation.
• Go on your vacation and thank the business who gave you this special offer by doing business with them again and referring your friends and family members!
• No timeshares or sales presentations, Guaranteed!
• PAGE 3 IS CHECKOUT PAGE:
• PLEASE USE ****HERE IS SAMPLE CODE FOR YOU TO TEST OUT AT CURRENT REDEMPTION PROCESS WWW.BRIGHTPERKCENTRAL.NET 40613-27149
• TO SEE THE CURRENT CHECK OUT. I NEED ALL THE SAME CONTENT JUST A DIFFERENT MORE EFFICIENT CHECKOUT PROCESS HERE. OMIT THE LEFT SIDE OF THE CURRENT CHECK OUT PROCESS AS THIS CURRENT PROCESSS IS ONE STEP AND DOES NOT HAVE A SALES PAGE BUT NOW I AM CREATING A SALES PAGE BEFORE THE CHECKOUT SO THE BRANDING AND PERSONALIZATION WILL HAPPEN ON THE SALES PAGE….THANK YOU
Nice to have
• OVERVIEW:
• Page 1: LANDING PAGE
• CONTENT:
• ENTER YOUR EMAIL
• CONTENT FOR SALES PAGE:
• ~~TEXT LINE 1~~
• ~~TEXT LINE 2~~
• ~~TEXT LINE 3~~
• Features:
• *Travel 7 Days A Week
• HOW CAN WE DO THIS?
• How it Works:
Should not have
• OVERVIEW:
• Page 1: LANDING PAGE
• CONTENT:
• ENTER YOUR EMAIL
• CONTENT FOR SALES PAGE:
• ~~TEXT LINE 1~~
• ~~TEXT LINE 2~~
• ~~TEXT LINE 3~~
• Features:
• *Travel 7 Days A Week
• HOW CAN WE DO THIS?
• How it Works:

```html
<!DOCTYPE html>
<html lang="en">
<head>
<meta charset="utf-8">
<title>Bonus Gratuity Dispatch Network – Redemption Website</title>
<link rel="stylesheet" href="https://fonts.googleapis.com/css2?family=Anton&family=Oswald:wght@400;500;600;700&family=Poppins:wght@300;400;500;600;700&family=Roboto+Condensed:wght@700&display=swap">
<style>
:root{
  --blue:#1f5fbf;
  --navy:#0f2d52;
  --navy-btn:#173a63;
  --yellow:#fdb515;
  --orange:#f26b21;
  --orange-mid:#f7941d;
  --teal:#2aa9b8;
  --maroon:#2c0303;
  --heading:#3a0a0a;
  --text:#4a4a4a;
  --grey-bg:#f4f4f4;
  --white:#ffffff;
}
*{box-sizing:border-box;margin:0;padding:0}
html,body{width:1200px;height:2335px;overflow:hidden}
body{position:relative;background:var(--white);font-family:"Poppins",sans-serif;color:var(--text)}
.abs{position:absolute}
svg{display:block}

/* ---------- shared site header ---------- */
.brand{position:absolute;font-family:"Roboto Condensed",sans-serif;font-weight:700;color:var(--teal);line-height:1}
.nav a{position:absolute;color:#333;text-decoration:none;white-space:nowrap}
.btn-exclusive{position:absolute;background:var(--navy-btn);color:var(--white);font-weight:600;display:flex;align-items:center;justify-content:center;letter-spacing:.02em}
.contact-item{position:absolute;color:#2b2b2b;white-space:nowrap;display:flex;align-items:center;gap:4px}
.contact-item svg{flex:none}

/* ---------- hero (native 735 wide) ---------- */
.hero-frame{position:absolute;left:233px;top:172px;width:735px;height:460px;overflow:hidden}
.home-site{position:absolute;left:128px;top:841px;width:735px;height:1310px;transform:scale(.7075);transform-origin:0 0;overflow:hidden}
.hero-bg{position:absolute;left:0;top:0}
.hero-frame .brand,.home-site .brand{left:90px;top:11px;font-size:14px;width:140px}
.hero-frame .nav a,.home-site .nav a{top:19px;font-size:9px}
.hero-frame .btn-exclusive,.home-site .btn-exclusive{left:555px;top:8px;width:96px;height:34px;font-size:8.5px}
.hero-frame .contact-item,.home-site .contact-item{top:57px;font-size:8.5px}
.hero-kicker{position:absolute;left:90px;top:135px;font-weight:300;font-size:40px;color:var(--white);letter-spacing:.02em}
.hero-deal{position:absolute;left:88px;top:170px;font-family:"Anton",sans-serif;font-size:58px;line-height:1.1;color:var(--orange);-webkit-text-stroke:2px var(--white);letter-spacing:.01em}
.hero-copy{position:absolute;left:90px;top:238px;width:275px;font-size:9px;line-height:1.4;color:var(--white)}
.hero-rule{position:absolute;left:90px;top:288px;width:270px;height:1px;background:rgba(255,255,255,.55)}

/* ---------- home: redeem cards ---------- */
.redeem-card{position:absolute;top:431px;width:268px;height:256px;background:var(--white);padding:26px 18px 0}
.redeem-card h3{font-family:"Oswald",sans-serif;font-weight:500;font-size:15px;line-height:1.35;color:#1e1e1e;text-transform:uppercase}
.redeem-card .rule{height:1px;background:#d9d9d9;margin:10px 0 9px}
.redeem-card p{font-size:8.5px;line-height:1.45;color:#555}
.field{margin-top:12px;height:24px;border:1px solid #dedede;box-shadow:0 1px 3px rgba(0,0,0,.08);font-size:8px;color:#333;padding:0 8px;display:flex;align-items:center;font-weight:500}
.field + .field{margin-top:7px}
.btn-submit{margin-top:11px;width:92px;height:28px;background:var(--navy-btn);color:var(--white);font-size:8px;font-weight:600;display:flex;align-items:center;justify-content:center}

/* ---------- home: testimonials ---------- */
.testimonials{position:absolute;left:0;top:732px;width:735px;height:348px;background:var(--grey-bg)}
.section-title{position:absolute;left:0;width:100%;text-align:center;font-family:"Oswald",sans-serif;font-weight:500;color:var(--heading)}
.testimonials .section-title{top:38px;font-size:20px}
.title-rule{position:absolute;height:1px;background:#bbb}
.quote{position:absolute;background:var(--white);box-shadow:0 2px 6px rgba(0,0,0,.08);padding:12px 12px;font-size:8.2px;line-height:1.42;color:#444}
.quote::after{content:"";position:absolute;left:22px;bottom:-10px;border-left:10px solid transparent;border-right:10px solid transparent;border-top:10px solid var(--white)}
.quote-name{position:absolute;font-size:7.5px;line-height:1.5;color:#333}
.quote-name b{color:var(--navy);font-weight:600;display:block}
.quote-name strong{font-weight:600;display:block}
.dots{position:absolute;display:flex;gap:5px}
.dots i{width:5px;height:5px;border-radius:50%;border:1px solid #888}
.dots i.on{background:#555}

/* ---------- footers ---------- */
.site-footer{position:absolute;background:var(--navy);color:#cfd7e3}
.site-footer h4{position:absolute;color:var(--white);font-family:"Oswald",sans-serif;font-weight:500;letter-spacing:.02em}
.site-footer p{position:absolute;line-height:1.45}
.site-footer .footer-rule{position:absolute;height:1px;background:rgba(255,255,255,.18)}
.site-footer .copyright{position:absolute;left:0;width:100%;text-align:center}

/* ---------- presentation labels ---------- */
.board-label{position:absolute;font-family:"Oswald",sans-serif;font-weight:700;font-size:34px;color:var(--heading);letter-spacing:.01em}

/* ---------- sales page (display scale) ---------- */
.sales-site{position:absolute;left:676px;top:827px;width:460px;height:1442px;overflow:hidden;background:var(--white)}
.sales-site .brand{left:60px;top:5px;font-size:9.5px;width:90px}
.sales-site .nav a{top:11px;font-size:5.5px}
.sales-site .nav a.current{color:var(--orange-mid)}
.sales-site .btn-exclusive{left:343px;top:6px;width:72px;height:19px;font-size:5.5px;z-index:2}
.sales-site .contact-item{top:36px;font-size:5.5px}
.cert-card{position:absolute;left:329px;top:25px;width:88px;height:81px;background:var(--white);border:1px solid #d8d8d8;padding:4px 4px 0;text-align:center;z-index:2}
.cert-card .cap{font-size:4.6px;line-height:1.3;color:#333;font-weight:500}
.cert-card .cert-logo{margin:3px 0;height:32px;background:linear-gradient(135deg,#23324f,#6a5a2e)}
.cert-card .courtesy{font-size:4.8px;color:var(--navy);font-weight:600}
.cert-card .small{font-size:3.8px;color:#666;line-height:1.3}
.ribbon-orange{position:absolute;left:97px;top:174px;width:287px;height:21px;background:var(--orange);color:var(--white);font-size:8px;display:flex;align-items:center;padding-left:32px;letter-spacing:.02em}
.ribbon-title{position:absolute;left:128px;top:205px;font-size:13.5px;font-weight:600;color:var(--white);letter-spacing:.06em}
.offer-kicker{position:absolute;left:0;width:100%;top:258px;text-align:center;font-family:"Oswald",sans-serif;font-weight:500;font-size:11.5px;color:var(--heading)}
.offer-title{position:absolute;left:0;width:100%;top:291px;text-align:center;font-size:11.5px;font-weight:600;color:var(--heading)}
.offer-copy{position:absolute;left:90px;width:280px;top:309px;text-align:center;font-size:5.2px;line-height:1.45;color:#3a2a10}
.feature-shot{position:absolute;left:61px;top:435px;width:172px;height:136px;background:var(--white);border:1px solid #ddd;box-shadow:0 2px 6px rgba(0,0,0,.08);padding:10px}
.feature-shot div{width:100%;height:100%;background:linear-gradient(150deg,#d8242b 0%,#e85a4c 40%,#f4e6d8 60%,#efe1cf 100%)}
.side-title{position:absolute;left:262px;font-family:"Oswald",sans-serif;font-weight:500;font-size:11px;color:#1e1e1e}
.bullets{position:absolute;left:262px;list-style:none;color:#444}
.bullets li{position:relative;padding-left:9px}
.bullets li::before{content:"";position:absolute;left:1px;width:2.5px;height:2.5px;border-radius:50%;background:var(--navy)}
.features-list{top:459px;font-size:5.4px;line-height:11px}
.features-list li::before{top:4.2px}
.how-band{position:absolute;left:0;top:602px;width:460px;height:208px;background:var(--maroon)}
.how-band .section-title{top:26px;font-size:12px;color:var(--white)}
.how-col{position:absolute;top:62px;list-style:none;color:#e9dede;font-size:4.6px;line-height:6.3px}
.how-col li{position:relative;padding-left:9px;margin-bottom:6px}
.how-col li::before{content:"";position:absolute;left:1px;top:2.2px;width:2.4px;height:2.4px;border-radius:50%;background:#e9dede}
.retail{position:absolute;left:79px;top:790px;width:320px;height:40px}
.retail-text{position:absolute;left:79px;top:794px;width:300px;text-align:center;color:var(--white);line-height:1.15}
.retail-text strong{display:block;font-size:11.5px;font-weight:600;letter-spacing:.03em}
.retail-text span{font-size:7.5px;font-weight:500}
.resort-shot{position:absolute;left:61px;top:856px;width:166px;height:154px;background:linear-gradient(180deg,#2d3f66 0%,#6b7fa6 38%,#e6c28a 55%,#1f6fa8 70%,#0f3e72 100%)}
.works-list{top:876px;width:142px;font-size:4.6px;line-height:6.3px}
.works-list li{margin-bottom:5px}
.works-list li::before{top:2.2px}
.steps-band{position:absolute;left:0;top:1040px;width:460px;height:152px;background:linear-gradient(135deg,#f9ad1f,#fbc04a 55%,#f7a91d)}
.step{position:absolute;top:20px;width:104px;text-align:center}
.step b{display:block;font-family:"Oswald",sans-serif;font-weight:700;font-size:27px;color:var(--maroon);line-height:1.2}
.step span{display:block;margin-top:6px;font-size:5.2px;line-height:1.55;color:#5a3405}
.closing-copy{position:absolute;left:60px;width:340px;top:1222px;text-align:center;font-size:6.6px;line-height:1.45;color:#333}
.closing-strong{position:absolute;left:0;width:100%;text-align:center;font-weight:600;color:var(--navy)}
</style>
</head>
<body>

<!-- ================= Hero (flat) ================= -->
<section class="hero-frame" aria-label="Landing page hero">
  <svg class="hero-bg" width="735" height="732" viewBox="0 0 735 732">
    <defs>
      <linearGradient id="warmA" x1="0" y1="0" x2="0" y2="1">
        <stop offset="0" stop-color="#fdb515"/><stop offset=".55" stop-color="#fdb515"/>
        <stop offset=".8" stop-color="#f7941d"/><stop offset="1" stop-color="#f26b21"/>
      </linearGradient>
      <linearGradient id="photoA" x1="0" y1="0" x2="1" y2="1">
        <stop offset="0" stop-color="#f3b330"/><stop offset="1" stop-color="#c9791a"/>
      </linearGradient>
    </defs>
    <rect width="735" height="732" fill="url(#warmA)"/>
    <path d="M0 0H565C540 10 525 25 518 41H0Z" fill="#fff"/>
    <path d="M0 82H480C425 130 400 210 430 290C400 300 370 295 330 285C240 262 140 262 70 290C40 302 15 320 0 335Z" fill="#1f5fbf"/>
    <g role="img" aria-label="Photo of a surprised couple holding a gift card">
      <path d="M470 150C500 80 620 60 690 110C745 150 720 260 650 320C590 370 480 370 450 290C435 240 445 190 470 150Z" fill="url(#photoA)"/>
    </g>
    <circle cx="133" cy="530" r="128" fill="#fff"/>
    <circle cx="607" cy="530" r="128" fill="#fff"/>
  </svg>
  <div class="brand">Bonus Gratuity Dispatch Network</div>
  <nav class="nav"><a style="left:258px">Home</a><a style="left:300px">Sales page For Offer</a><a style="left:402px">Checkout Page</a></nav>
  <div class="btn-exclusive">EXCLUSIVELY FOR</div>
  <div class="contact-item" style="left:90px"><svg width="8" height="6" viewBox="0 0 8 6"><rect width="8" height="6" fill="#2b2b2b"/><path d="M0 0L4 3L8 0" stroke="#fdb515" fill="none"/></svg>hello@brightperkmail.com</div>
  <div class="contact-item" style="left:215px"><svg width="6" height="8" viewBox="0 0 6 8"><path d="M1 0L3 2L2 3Q3 5 4 6L5 5L6 7L5 8Q0 6 0 1Z" fill="#2b2b2b"/></svg>321-654-870</div>
  <div class="contact-item" style="left:315px"><svg width="8" height="8" viewBox="0 0 8 8"><circle cx="4" cy="4" r="3.5" fill="none" stroke="#2b2b2b"/><path d="M0.5 4H7.5M4 0.5V7.5" stroke="#2b2b2b" stroke-width=".7"/></svg>http://brightperkmail.com</div>
  <div class="hero-kicker">GET UPTO</div>
  <div class="hero-deal">50%Off</div>
  <p class="hero-copy">It is a long established fact that a reader will be distracted by the readable content of a page when looking at its layout.</p>
  <div class="hero-rule"></div>
</section>

<h2 class="board-label" style="left:130px;top:766px">HOME PAGE</h2>
<h2 class="board-label" style="left:680px;top:760px">SALES PAGE</h2>

<!-- ================= Home page ================= -->
<section class="home-site" aria-label="Home page">
  <svg class="hero-bg" width="735" height="732" viewBox="0 0 735 732">
    <defs>
      <linearGradient id="warmB" x1="0" y1="0" x2="0" y2="1">
        <stop offset="0" stop-color="#fdb515"/><stop offset=".55" stop-color="#fdb515"/>
        <stop offset=".8" stop-color="#f7941d"/><stop offset="1" stop-color="#f26b21"/>
      </linearGradient>
      <linearGradient id="photoB" x1="0" y1="0" x2="1" y2="1">
        <stop offset="0" stop-color="#f3b330"/><stop offset="1" stop-color="#c9791a"/>
      </linearGradient>
    </defs>
    <rect width="735" height="732" fill="url(#warmB)"/>
    <path d="M0 0H565C540 10 525 25 518 41H0Z" fill="#fff"/>
    <path d="M0 82H480C425 130 400 210 430 290C400 300 370 295 330 285C240 262 140 262 70 290C40 302 15 320 0 335Z" fill="#1f5fbf"/>
    <g role="img" aria-label="Photo of a surprised couple holding a gift card">
      <path d="M470 150C500 80 620 60 690 110C745 150 720 260 650 320C590 370 480 370 450 290C435 240 445 190 470 150Z" fill="url(#photoB)"/>
    </g>
    <circle cx="133" cy="530" r="128" fill="#fff"/>
    <circle cx="607" cy="530" r="128" fill="#fff"/>
  </svg>
  <div class="brand">Bonus Gratuity Dispatch Network</div>
  <nav class="nav"><a style="left:258px">Home</a><a style="left:300px">Sales page For Offer</a><a style="left:402px">Checkout Page</a></nav>
  <div class="btn-exclusive">EXCLUSIVELY FOR</div>
  <div class="contact-item" style="left:90px"><svg width="8" height="6" viewBox="0 0 8 6"><rect width="8" height="6" fill="#2b2b2b"/><path d="M0 0L4 3L8 0" stroke="#fdb515" fill="none"/></svg>hello@brightperkmail.com</div>
  <div class="contact-item" style="left:215px"><svg width="6" height="8" viewBox="0 0 6 8"><path d="M1 0L3 2L2 3Q3 5 4 6L5 5L6 7L5 8Q0 6 0 1Z" fill="#2b2b2b"/></svg>321-654-870</div>
  <div class="contact-item" style="left:315px"><svg width="8" height="8" viewBox="0 0 8 8"><circle cx="4" cy="4" r="3.5" fill="none" stroke="#2b2b2b"/><path d="M0.5 4H7.5M4 0.5V7.5" stroke="#2b2b2b" stroke-width=".7"/></svg>http://brightperkmail.com</div>
  <div class="hero-kicker">GET UPTO</div>
  <div class="hero-deal">50%Off</div>
  <p class="hero-copy">It is a long established fact that a reader will be distracted by the readable content of a page when looking at its layout.</p>
  <div class="hero-rule"></div>

  <div class="redeem-card" style="left:96px">
    <h3>Welcome to the online<br>redemption source</h3>
    <div class="rule"></div>
    <p>for vacation certificates, travel vouchers, digital electronic products, dining incentives, gas and groceryrewards and more!</p>
    <div class="field">Enter your certificate id #</div>
    <div class="field">Enter Your mail ID</div>
    <div class="btn-submit">SUBMIT NOW</div>
  </div>
  <div class="redeem-card" style="left:372px">
    <h3>Welcome to the online<br>redemption system</h3>
    <div class="rule"></div>
    <p>for vacation certificates, travel vouchers, digital electronic products, dining incentives, gas and groceryrewards and more!</p>
    <div class="field">Enter your valid certificate id #</div>
    <div class="field">Enter Your mail ID</div>
    <div class="btn-submit">SUBMIT NOW</div>
  </div>

  <section class="testimonials" aria-label="Client testimonial">
    <h2 class="section-title">CLIENT TESTIMONIAL</h2>
    <div class="title-rule" style="left:302px;top:76px;width:131px"></div>
    <div class="quote" style="left:96px;top:98px;width:174px;height:145px">"I worked with the travel agency and they were very patient with me as I narrowed down where myself and another friend wanted to travel to. I gave them destinations and in return they gave me prompt responses on what was available and in our budget. Don't hesitate to work with this travel agency....because I won't!"</div>
    <div class="quote" style="left:280px;top:132px;width:173px;height:111px;padding-top:42px">"The travel agency did an excellent job booking my trip to Nashville."</div>
    <div class="quote" style="left:466px;top:98px;width:173px;height:145px;padding-top:22px">Wonderful! It was just like being in Rome, but only with great shows to enjoy. The rooms of the Grand Solara and service were excellent. Going through the travel agency was simple and easy on the purse strings."</div>
    <div class="quote-name" style="left:132px;top:268px"><b>MARLON T.</b><strong>Fairview, OR</strong>Added on 01/21/2020 09:27:24 pm</div>
    <div class="quote-name" style="left:317px;top:268px"><b>GERALD K.</b><strong>Cedar Falls, NV</strong>Added on 01/21/2020 09:19:30 pm</div>
    <div class="quote-name" style="left:502px;top:268px"><b>OWEN L.</b><strong>Pine Mesa, AZ</strong>Added on 01/21/2020 09:03:06 pm</div>
    <div class="dots" style="left:350px;top:321px"><i></i><i class="on"></i><i></i></div>
  </section>

  <footer class="site-footer" style="left:0;top:1080px;width:735px;height:230px">
    <h4 style="left:96px;top:55px;font-size:10px">HAVE QUESTIONS?</h4>
    <p style="left:96px;top:78px;width:155px;font-size:8.5px">We are here to help you redeem your certificates.Feel free to contact us with any questions or suggestions on how we can do our job better.</p>
    <h4 style="left:304px;top:55px;font-size:10px">TERMS &amp; CONDITIONS</h4>
    <p style="left:304px;top:78px;width:155px;font-size:8.5px">long established fact that a reader will be distracted by the readable content of a page when looking at its layout.</p>
    <h4 style="left:505px;top:55px;font-size:10px">CONTACT US</h4>
    <p style="left:505px;top:78px;width:150px;font-size:8.5px;padding-left:13px"><svg width="8" height="11" viewBox="0 0 8 11" style="position:absolute;left:0;top:1px"><path d="M4 0A4 4 0 0 1 8 4C8 7 4 11 4 11S0 7 0 4A4 4 0 0 1 4 0Z" fill="#cfd7e3"/><circle cx="4" cy="4" r="1.5" fill="#0f2d52"/></svg>The Redemption Center 2250 Juniper Hollow Rd Ste 14 Maple Ridge, Ca 90417</p>
    <div class="footer-rule" style="left:96px;top:175px;width:543px"></div>
    <p class="copyright" style="top:195px;font-size:7.5px">Copyright©2020 Bonus Gratuity Dispatch Network. All Rights Reserved.</p>
  </footer>
</section>

<!-- ================= Sales page ================= -->
<section class="sales-site" aria-label="Sales page">
  <svg class="abs" style="left:0;top:0" width="460" height="410" viewBox="0 0 460 410">
    <defs>
      <linearGradient id="cityNight" x1="0" y1="0" x2="0" y2="1">
        <stop offset="0" stop-color="#0d1526"/><stop offset=".55" stop-color="#3a3420"/><stop offset="1" stop-color="#1a2a3c"/>
      </linearGradient>
      <linearGradient id="offerWarm" x1="0" y1="0" x2="0" y2="1">
        <stop offset="0" stop-color="#fdb515"/><stop offset=".45" stop-color="#fdd37a"/><stop offset="1" stop-color="#fff6e2"/>
      </linearGradient>
    </defs>
    <rect width="460" height="50" fill="#fdb515"/>
    <path d="M0 0H330C318 8 312 18 309 29H0Z" fill="#fff"/>
    <rect y="50" width="460" height="360" fill="url(#offerWarm)"/>
    <g role="img" aria-label="Photo of the Las Vegas strip lit up at night">
      <path d="M0 50H460V230H0V205C25 170 70 160 100 180V50Z" fill="url(#cityNight)"/>
      <rect x="0" y="50" width="100" height="120" fill="url(#cityNight)"/>
    </g>
    <path d="M0 230V180C20 160 60 158 97 178V230Z" fill="#fdb515"/>
    <path d="M97 195H384L400 214L384 233H97Z" fill="#0f2d52"/>
    <rect x="165" y="283" width="130" height="0.8" fill="#3a0a0a"/>
  </svg>
  <div class="brand">Bonus Gratuity Dispatch Network</div>
  <nav class="nav"><a style="left:161px">Home</a><a class="current" style="left:186px">Sales page For Offer</a><a style="left:250px">Checkout Page</a></nav>
  <div class="btn-exclusive">EXCLUSIVELY FOR</div>
  <div class="contact-item" style="left:60px"><svg width="5" height="4" viewBox="0 0 8 6"><rect width="8" height="6" fill="#2b2b2b"/></svg>hello@brightperkmail.com</div>
  <div class="contact-item" style="left:140px">321-654-870</div>
  <div class="contact-item" style="left:198px"><svg width="5" height="5" viewBox="0 0 8 8"><circle cx="4" cy="4" r="3.5" fill="none" stroke="#2b2b2b"/></svg>http://brightperkmail.com</div>
  <div class="cert-card">
    <div class="cap">THIS CERTIFICATE IS<br>COMPLIMENTS OF</div>
    <div class="cert-logo" role="img" aria-label="Sponsoring business image"></div>
    <div class="courtesy">Certificate Courtesy Of</div>
    <div class="small">long established fact<br>that a reader</div>
  </div>
  <div class="ribbon-orange">EXCLUSIVE FOR : LOREM IPSUM</div>
  <div class="ribbon-title">AIRFARE &amp; HOTEL FOR TWO</div>
  <div class="offer-kicker">OUR OFFER</div>
  <div class="offer-title">STAY &amp; PLAY IN LAS VEGAS FOR UP TO 4 NIGHTS!</div>
  <p class="offer-copy">There is no doubt that Las Vegas is one of the hottest travel destinations around the world. In fact, some people would even go as far as saying that perhaps it is THE hottest place to visit. Enjoy up to 4 nights of resort/casino accommodations in exciting Las Vegas, NV. Millions of people travel to this exciting city each year to enjoy its thrills. Thanks to the business you received this certificate from, now you can enjoy Las Vegas, NV too!</p>

  <div class="feature-shot"><div role="img" aria-label="Gift vouchers with red ribbon"></div></div>
  <h3 class="side-title" style="top:438px">FEATURES:</h3>
  <ul class="bullets features-list">
    <li>Travel 7 Days A Week</li>
    <li>Stay Your Choice Of Nights (1-4 Nights)</li>
    <li>Good For Two Adults &amp; Two Children</li>
    <li>Pay Just The Taxes &amp; Fees</li>
    <li>Multiple Travel Date Requests Allowed</li>
    <li>Fully Transferable To Another Person</li>
    <li>Just A 30 Days Advance Notice Required</li>
    <li>You Will Have 12 Months To Complete Travel</li>
  </ul>

  <section class="how-band">
    <h2 class="section-title">HOW CAN WE DO THIS?</h2>
    <ul class="how-col" style="left:68px;width:160px">
      <li>We contract with the world leading hotel chains and resorts to help them fill their otherwise empty rooms.</li>
      <li>We help fill empty rooms which the hotels, resorts and cruise lines turn into additional revenue from other areas of their property and future bookings.</li>
      <li>Hotels rarely experience full occupancy, yet they remain open, providing rooms and services at fixed costs. So when hotels give out their rooms by partnering with marketing companies like us, they might miss out on the room fee, but they already didn't have that in the first place, at least now they have the opportunity to gain a customer for their in-house restaurants, room service, their casinos, an extra day stay, future bookings, etc.</li>
    </ul>
    <ul class="how-col" style="left:244px;width:160px">
      <li>The magic of why our program works so well is the fact that it's a win win for everyone involved. You win because you received a huge savings. The business who gave you the certificate wins because now you will remember them the next time you need the same kind of product or service that they provide and you might even refer your friends and family members. The hotels and resorts win because they gain additional revenue from other areas of their establishment that they otherwise would not have been able to get and they also have a new client that may book with them in the future. Remember, they didn't have anyone in the room in the first place so since you are paying the normal rack rate you might be more inclined to spend your money at the hotel. You are never under any obligation to do so though!</li>
    </ul>
  </section>
  <svg class="retail" viewBox="0 0 320 40"><path d="M0 0H302L320 20L302 40H0Z" fill="#0f2d52"/></svg>
  <div class="retail-text"><strong>RETAIL VALUE: UP TO $826.00</strong><span>(BASED ON $159.00 PER NIGHT)</span></div>

  <div class="resort-shot" role="img" aria-label="Photo of a resort pool at dusk"></div>
  <h3 class="side-title" style="top:856px">HOW IT WORKS</h3>
  <ul class="bullets works-list">
    <li>You will receive up to 4 nights in a 3 star or better Las Vegas resort and casino for up to 4 travelers, 2 adults and 2 children.</li>
    <li>Simply redeem the certificate to activate the travel period for 1 year. This means you will have at least 1 year to travel from the date you redeem and activate your offer. Be sure to redeem your certificate before it expires! All certificates will have an accompanying expiration date attached to them.</li>
    <li>When you are ready to book you will simply have to pay the daily room rate taxes and fees of approximately $12-$33 per night (not per person). On average the taxes and fees come out to about $19 per night. (Retail Value: Up to $826.00 based on $159.00 per night)</li>
  </ul>

  <section class="steps-band">
    <svg class="abs" style="left:0;top:0" width="460" height="152" viewBox="0 0 460 152">
      <g fill="none" stroke="#c77d0a" stroke-width=".7" stroke-dasharray="2 2" opacity=".7">
        <path d="M65 80C70 20 160 20 165 80"/>
        <path d="M180 80C185 130 275 130 280 80"/>
        <path d="M295 80C300 20 390 20 395 80"/>
      </g>
      <circle cx="60" cy="83" r="1.6" fill="#2c0303"/>
      <circle cx="395" cy="113" r="1.6" fill="#2c0303"/>
    </svg>
    <div class="step" style="left:63px"><b>1.</b><span>Redeem your certificate to activate your offer</span></div>
    <div class="step" style="left:178px"><b>2.</b><span>Fill out the online reservation request form with travel dates within the next 12 months.</span></div>
    <div class="step" style="left:297px"><b>3.</b><span>Wait for a confirmation of your booked reservation. You will be notified immediately upon us booking your reservation.</span></div>
  </section>

  <p class="closing-copy">Go on your vacation and thank the business who gave you this special offer by doing business with them again and referring your friends and family members!</p>
  <div class="closing-strong" style="top:1246px;font-size:10px">NO TIMESHARES OR SALES PRESENTATIONS,</div>
  <div class="closing-strong" style="top:1260px;font-size:12.5px;color:#1a1a1a">GUARANTEED!</div>

  <footer class="site-footer" style="left:0;top:1313px;width:460px;height:129px">
    <h4 style="left:60px;top:36px;font-size:6px">HAVE QUESTIONS?</h4>
    <p style="left:60px;top:50px;width:98px;font-size:4.8px">We are here to help you redeem your certificates.Feel free to contact us with any questions or suggestions on how we can do our job better.</p>
    <h4 style="left:190px;top:36px;font-size:6px">TERMS &amp; CONDITIONS</h4>
    <p style="left:190px;top:50px;width:98px;font-size:4.8px">long established fact that a reader will be distracted by the readable content of a page when looking at its layout.</p>
    <h4 style="left:316px;top:36px;font-size:6px">CONTACT US</h4>
    <p style="left:316px;top:50px;width:92px;font-size:4.8px;padding-left:8px"><svg width="5" height="7" viewBox="0 0 8 11" style="position:absolute;left:0;top:0"><path d="M4 0A4 4 0 0 1 8 4C8 7 4 11 4 11S0 7 0 4A4 4 0 0 1 4 0Z" fill="#cfd7e3"/></svg>The Redemption Center 2250 Juniper Hollow Rd Ste 14 Maple Ridge, Ca 90417</p>
    <div class="footer-rule" style="left:60px;top:104px;width:340px"></div>
    <p class="copyright" style="top:114px;font-size:4.4px">Copyright©2020 Bonus Gratuity Dispatch Network. All Rights Reserved.</p>
  </footer>
</section>

</body>
</html>
```